Design the Business card for NetVaultix

Business card required for a professional Cyber Security business.
Company Logo and Icon has already been provided however I would like other options for the logo and icon to compare to. Alternatively, please refine/enhance the image of the logo.icon I have already provided.

If you are going to use the provided logo and icon, I was thinking that the company raised Logo on White background would serve well on the front of the card. See attached. AND, a large company raised stand-alone icon to appear on black background on the back of the card with tagline 'Cyber Risk Management, Governance and Consulting' or 'Cyber Security for your Business' See attached.
Alternatively, provide your own design for the logo and icon.

Target Market(s)

Enterprise, Government, Financial.

Contact Information for Business Card

Teodor Vaskelin
Founder and CEO

Email Address
Mobile Number
Website URL
LinkedIn URL

Logo Text

NetVaultix - see attached example of logo

Font styles to use
Other font styles liked:
• Berlin Sans FB

Requirements
Must have
• Clean large and bold icon on the back with tagline.
• Horizontal alignment,
Nice to have
• Round edges.
• Raised Logo/Icon
Should not have
• An unprofessional look and feel.

```html
<!DOCTYPE html>
<html lang="en">
<head>
<meta charset="utf-8">
<title>NetVaultix Business Card</title>
<link rel="stylesheet" href="https://fonts.googleapis.com/css2?family=Lato:wght@400;700;900&family=Arimo:wght@400;700&display=swap">
<style>
  :root {
    --page-bg: #e9ebee;
    --card-white: #ffffff;
    --brand-blue: #1f6fc6;
    --band-blue: #4573c4;
    --accent-yellow: #f6b800;
    --ink-dark: #1d1d1f;
    --ink-light: #ffffff;
  }
  * { box-sizing: border-box; margin: 0; padding: 0; }
  html, body {
    width: 1200px; height: 900px; overflow: hidden;
    background: var(--page-bg);
  }
  .canvas {
    width: 1200px; height: 900px;
    display: flex; align-items: center; justify-content: center;
  }
  .business-card {
    width: 960px; height: 598px;
    background: var(--card-white);
    display: flex; flex-direction: column;
    box-shadow: 0 10px 30px rgba(0,0,0,0.12);
  }
  .card-top {
    height: 340px;
    display: flex; flex-direction: column; align-items: center;
    padding-top: 92px;
  }
  .brand {
    display: flex; align-items: center; gap: 22px;
  }
  .brand-mark {
    width: 84px; height: 84px; border-radius: 50%;
    background: var(--brand-blue);
  }
  .brand-name {
    font-family: "Lato", sans-serif; font-weight: 900;
    font-size: 86px; line-height: 1; color: var(--brand-blue);
    letter-spacing: -0.5px;
  }
  .tagline {
    margin-top: 44px;
    font-family: "Lato", sans-serif; font-weight: 400;
    font-size: 22px; letter-spacing: 0.6px; color: var(--ink-dark);
  }
  .accent-rule {
    height: 7px; background: var(--accent-yellow);
  }
  .card-band {
    flex: 1;
    background: var(--band-blue);
    display: flex; justify-content: space-between; align-items: flex-start;
    padding: 56px 66px 0 56px;
  }
  .contact-list { list-style: none; }
  .contact-item {
    display: flex; align-items: center; gap: 12px;
    font-family: "Arimo", sans-serif; font-size: 26px;
    color: var(--ink-light); line-height: 35px;
  }
  .contact-icon { width: 20px; height: 20px; flex: none; }
  .person { text-align: right; font-family: "Arimo", sans-serif; }
  .person-name {
    font-weight: 700; font-size: 35px; color: var(--accent-yellow);
    letter-spacing: 0.3px; line-height: 1.1;
  }
  .person-role {
    font-size: 27px; color: var(--ink-light); line-height: 1.2;
  }
</style>
</head>
<body>
<main class="canvas">
  <article class="business-card">
    <section class="card-top">
      <div class="brand">
        <span class="brand-mark" aria-hidden="true"></span>
        <span class="brand-name">NetVaultix</span>
      </div>
      <p class="tagline">CYBER RISK MANAGEMENT, GOVERNANCE AND CONSULTING</p>
    </section>
    <div class="accent-rule"></div>
    <section class="card-band">
      <ul class="contact-list">
        <li class="contact-item">
          <svg class="contact-icon" viewBox="0 0 20 20" aria-hidden="true">
            <path fill="#f6b800" d="M2 7c0-2 3-4 8-4s8 2 8 4v1h-4V6.5H6V8H2z M5 9h10l2 7H3z"/>
            <circle cx="10" cy="12.5" r="2" fill="#4573c4"/>
          </svg>
          044-987 654 321
        </li>
        <li class="contact-item">
          <svg class="contact-icon" viewBox="0 0 20 20" aria-hidden="true">
            <rect x="2" y="4" width="16" height="12" fill="#f6b800"/>
            <path d="M2 4l8 7 8-7" fill="none" stroke="#4573c4" stroke-width="1.6"/>
          </svg>
          info@netvaultix.com
        </li>
        <li class="contact-item">
          <svg class="contact-icon" viewBox="0 0 20 20" aria-hidden="true">
            <circle cx="10" cy="10" r="8" fill="#f6b800"/>
            <path d="M6 6c2 1 3 0 4 2s-2 3 0 5M13 5c-1 2 1 3 2 4" fill="none" stroke="#4573c4" stroke-width="1.5"/>
          </svg>
          www.netvaultix.com
        </li>
        <li class="contact-item">
          <svg class="contact-icon" viewBox="0 0 20 20" aria-hidden="true">
            <rect x="2" y="2" width="16" height="16" fill="#f6b800"/>
          </svg>
          www.profiles.net/netvaultix
        </li>
      </ul>
      <div class="person">
        <p class="person-name">TEODOR VASKELIN</p>
        <p class="person-role">Founder and CEO</p>
      </div>
    </section>
  </article>
</main>
</body>
</html>
```